Childrens summer camp Flier/ And Rhythmic Gymnastics Intensive

We are looking for a Two sided flier, one side of flier is a advertisement for Childrens Multi Sport Summer Camp at our gym.
The other side is Rhythmic Gymnastics Intensive Program.

These are two very different programs. The Summer camp is for kids ages 4-15, where they can choose from many sports and do arts and crafts, but the Rhythmic is a very Intense Rhythmic program for our professional gymnastics to advance skills. It is a very serious program.

Websites:
www.vortaflipmiami.example - Camp side (786) 555-0142
www.vortaflipathletics.example - Intensive side (786) 555-0187

We want the Summer Camp side to be fun and playful, Showing the different sports available,
-Artistic Gymnastics
-Silk/ Aerial
-Kickboxing
-Trampoline and Tumbling
-Recreational/ Introductory to Rhythmic Gymnastics
-Games
-Arts & Crafts
-Weekly Field trips,
-Healthy Lunch & Snacks Available
- Half day/ Full day & Extended day camps available

Rhythmic Intensive:
• Advanced Choreography; Russian Classical Ballet Training
• Ballet Point Shoe Training
• Body Development and Strength Training
• Advanced Rhythmic Gymnastics Element Mastery
• Advanced Mastery of Equipment Handling & Super Tricks
• Routine Development
• Extreme Stretching
• Body Conditioning
• Dance Classes
• Nutrition Education (include meals preparation, diet and weight management)
• Code of Points ; Score Cards Instruction
• Catered Lunch ; Snacks (Healthy Russian Food) Available
• Weekly Field Trips (Museums & Cultural Centers, Water & Amusement Parks, the Beach, Horseback Riding, Ballet and Dance Performance Shows and other memorable summer events)
• Camping & Overnight Trips (additional fees will apply for camping and overnight trips)

Camp takes place in our NEW facility.
2 NEW professional Carpets
Professional conditioning bands and bars provided
- New "Air-conditioned" gymnasium
Mirrors
Professional Ballet Bars
Professional World Class Coaches

Rhythmic Levels 3-10

Vortaflip/ Vortaflip School of Gymnastics
48760 NE 92nd Ave
North Miami FL 33181

(786) 555-0142

Target Market(s)

Side 1 - Moms looking for a camp for children ages 4-15 in the summer.
Side 2 - Rhythmic Gymnasts currently in other schools, who want to advance skills beyond current capability with floridas leading School

Industry/Entity Type

Gym

Font styles to use
Serif
Sans Serif
Decorative

Colors
0456a4
3277b5
886aae
ffffff
6b449b
ec1f27
e34197
85acd3
cfdfed

Requirements
Must have
• SIZE:
• Bleed Size: 4.25x6.25
• Size your image files to the Bleed Size to ensure your background extends to the edge of the card.
• Safe Zone: 3.75x5.75
• Illustrates the cutting margin. We can potentially cut the cards up to this point. Anything extending outside this area risks being trimmed.
• ---------------------------
• Must have Logos, Vortaflip on camp side and VortaflipAthletics on Rhythmic side.
• Address, phone websites
• Verbage
• Rhythmic advance pictures on Intensive side only, Small children Rhythmic on Summer camp side. These are two different programs and need to have separate feeling and messaging.
Should not have
• Other sports on the Rhythmic Intensive page
• Photos that are not posted below

```html
<!DOCTYPE html>
<html lang="en">
<head>
<meta charset="utf-8">
<title>Vortaflip Summer Camp Flier</title>
<link rel="stylesheet" href="https://fonts.googleapis.com/css2?family=Chewy&family=Gochi+Hand&family=Open+Sans:wght@700&display=swap">
<style>
  :root {
    --page-bg: #b9bec6;
    --band-dark: #393d45;
    --stripe-red: #ec1f27;
    --camp-pink: #e34197;
    --camp-purple: #886aae;
    --deep-purple: #6b449b;
    --night-blue: #2c3473;
    --ink: #2f2b3a;
    --white: #ffffff;
    --light-blue: #85acd3;
    --soft-grey: #d6d8dc;
  }
  * { box-sizing: border-box; margin: 0; padding: 0; }
  html, body { width: 1200px; height: 1000px; overflow: hidden; }
  body { background: var(--page-bg); position: relative; }

  .flier {
    position: absolute; left: 178px; top: 183px;
    width: 852px; height: 602px; overflow: hidden;
    background: var(--night-blue);
  }
  .hero-photo {
    position: absolute; inset: 0;
    background:
      radial-gradient(ellipse 420px 520px at 180px 300px, rgba(214,196,70,0.95), rgba(214,196,70,0) 75%),
      linear-gradient(90deg, #c6b23a 0%, #9f9442 30%, #5a5a6e 48%, #34377a 62%, #2c3473 100%);
  }
  .bubble {
    position: absolute; border-radius: 50%;
    border: 3px solid var(--white);
  }
  .kids-photo {
    left: 379px; top: -1px; width: 156px; height: 156px;
    background: radial-gradient(circle at 45% 45%, #f2c9a6, #d98a5a 55%, #6f8fb0 100%);
  }
  .activities {
    left: 168px; top: 113px; width: 284px; height: 296px;
    background: var(--camp-pink);
    display: flex; flex-direction: column; align-items: center; justify-content: center;
    font-family: "Gochi Hand", cursive; color: var(--white);
    font-size: 16px; line-height: 21.4px; text-align: center; text-transform: uppercase;
    letter-spacing: 0.3px;
  }
  .facility {
    left: 532px; top: -30px; width: 380px; height: 372px;
    background: var(--camp-purple);
  }
  .facility-text {
    position: absolute; right: 18px; top: 18px; width: 300px;
    font-family: "Gochi Hand", cursive; color: var(--ink);
    text-transform: uppercase; text-align: right;
    font-size: 17px; line-height: 23px;
  }
  .facility-title {
    color: var(--white); font-size: 22px; line-height: 29px; margin-bottom: 6px;
  }
  .facility-text li { list-style: none; margin-bottom: 7px; }
  .levels {
    left: 465px; top: 257px; width: 120px; height: 120px;
    background: var(--camp-purple);
    display: flex; align-items: center; justify-content: center;
    font-family: "Gochi Hand", cursive; color: var(--white);
    font-size: 16px; line-height: 21px; text-align: center; text-transform: uppercase;
  }
  .accent-pink-a { left: 405px; top: 360px; width: 100px; height: 100px; background: var(--camp-pink); }
  .accent-pink-b { left: 565px; top: 330px; width: 95px; height: 95px; background: var(--camp-pink); }

  .footer-band { position: absolute; left: 0; top: 0; width: 852px; height: 602px; }
  .title-art { position: absolute; left: 0; top: 0; width: 852px; height: 602px; }
  .title-text { font-family: "Chewy", cursive; }

  .contact {
    position: absolute; left: 21px; top: 516px; font-style: normal;
    font-family: "Open Sans", sans-serif; font-weight: 700;
  }
  .contact .school { color: var(--light-blue); font-size: 16px; line-height: 22px; }
  .contact .address { color: var(--soft-grey); font-size: 16px; line-height: 24px; }
  .contact .address .divider { margin: 0 6px; }
  .contact .phone { color: var(--white); font-size: 27px; line-height: 36px; margin-top: 2px; }

  .brand {
    position: absolute; left: 512px; top: 470px;
    display: flex; align-items: center; gap: 12px;
    font-family: "Open Sans", sans-serif; font-weight: 700;
    font-size: 54px; color: var(--stripe-red); letter-spacing: -1px;
  }
  .brand-dot { width: 18px; height: 18px; border-radius: 50%; background: var(--stripe-red); }
</style>
</head>
<body>
  <main class="flier">
    <div class="hero-photo" role="img" aria-label="Photo of a young rhythmic gymnast in a backbend holding an orange ball on a golden studio background"></div>

    <div class="bubble kids-photo" role="img" aria-label="Photo of smiling young children lying together on a gym floor"></div>

    <div class="bubble facility"></div>
    <div class="facility-text">
      <p class="facility-title">Camp takes place in<br>our new facility.</p>
      <ul>
        <li>2 new professional carpets</li>
        <li>Professional conditioning<br>bands and bars provided</li>
        <li>"Air-conditioned"<br>gymnasium</li>
        <li>Mirrors &amp; ballet bars</li>
        <li>Professional coaches</li>
      </ul>
    </div>

    <div class="bubble accent-pink-a"></div>
    <div class="bubble accent-pink-b"></div>

    <div class="bubble activities">
      <span>Artistic Gymnastics</span>
      <span>Silk/ Aerial</span>
      <span>Kickboxing</span>
      <span>Trampoline and Tumbling</span>
      <span>Recreational/ Introductory</span>
      <span>to Rhythmic Gymnastics</span>
      <span>Games</span>
      <span>Arts &amp; Crafts</span>
      <span>Weekly Field Trips</span>
      <span>Healthy Russian Lunch</span>
      <span>Available $7 per day</span>
    </div>

    <div class="bubble levels">Rhythmic<br>Levels 3-10</div>

    <svg class="footer-band" viewBox="0 0 852 602" aria-hidden="true">
      <path d="M0 500 C 250 470, 560 420, 852 335 L 852 602 L 0 602 Z" fill="var(--stripe-red)"/>
      <path d="M0 507 C 250 478, 560 428, 852 342 L 852 602 L 0 602 Z" fill="var(--band-dark)"/>
    </svg>

    <svg class="title-art" viewBox="0 0 852 602" aria-hidden="true">
      <g class="title-text">
        <text x="34" y="494" font-size="96" textLength="470" lengthAdjust="spacingAndGlyphs" transform="rotate(-4 270 470)"
              fill="none" stroke="var(--white)" stroke-width="16" stroke-linejoin="round">SUMMER</text>
        <text x="34" y="494" font-size="96" textLength="470" lengthAdjust="spacingAndGlyphs" transform="rotate(-4 270 470)"
              fill="var(--deep-purple)" stroke="var(--band-dark)" stroke-width="6" paint-order="stroke" stroke-linejoin="round">SUMMER</text>
        <text x="545" y="412" font-size="92" textLength="280" lengthAdjust="spacingAndGlyphs" transform="rotate(-13 680 380)"
              fill="none" stroke="var(--white)" stroke-width="16" stroke-linejoin="round">CAMP</text>
        <text x="545" y="412" font-size="92" textLength="280" lengthAdjust="spacingAndGlyphs" transform="rotate(-13 680 380)"
              fill="var(--camp-pink)" stroke="var(--band-dark)" stroke-width="6" paint-order="stroke" stroke-linejoin="round">CAMP</text>
      </g>
    </svg>

    <div class="brand">
      <span class="brand-dot"></span>
      <span class="brand-name">Vortaflip</span>
    </div>

    <address class="contact">
      <p class="school">Vortaflip &amp; Vortaflip School of Gymnastics</p>
      <p class="address">48760 NE 92nd Ave<span class="divider">|</span>North Miami FL 33181</p>
      <p class="phone">Call Us (786) 555-0142</p>
    </address>
  </main>
</body>
</html>
```